Business Card Design

I am an independent consultant to the telecommunications industry. I specialize in helping equipment manufacturers of high end fiber optic telecommunications products market and sell their products to end users such as bk&q, Quelmar, Pine Harbor Cable, Stratum 9, Dovex, etc. I conduct this activity on a global or worldwide basis. I need a professional looking card that contains a high-tech telecommunications related logo. I am thinking of something along the lines of two telephone poles separated by a bright narrow beam of light (as opposed to traditional wire) and perhaps spanning a spherical globe (world).
Target Market(s)
Engineers, Executives and Purchasing Agents for Large Keystone 700 companies
Industry/Entity Type
Telecommunications
Contact Information for Business Card
Gil Harvey, President, Upland Signal Associates, LLC, 4826-Mercer Drive, Pilot Point, TX 76490-2817, 972-555-0148

```html
<!DOCTYPE html>
<html lang="en">
<head>
<meta charset="utf-8">
<title>Gil Harvey – Business Card</title>
<link href="https://fonts.googleapis.com/css2?family=Arimo:ital,wght@0,400;0,700;1,400&display=swap" rel="stylesheet">
<style>
  :root {
    --card-blue: #0060a8;
    --panel-white: #ffffff;
    --ink: #111111;
    --teal-light: #8fe0c6;
    --teal-dark: #2a6f78;
    --mist: #c9dcec;
  }
  html, body {
    margin: 0;
    padding: 0;
    overflow: hidden;
    background: #ffffff;
  }
  .card {
    position: relative;
    width: 1200px;
    height: 705px;
    background: var(--card-blue);
    overflow: hidden;
    font-family: "Arimo", Arial, sans-serif;
  }
  .backdrop {
    position: absolute;
    left: 0;
    top: 0;
  }
  .name-panel {
    position: absolute;
    left: 0;
    top: 169px;
    width: 704px;
    height: 228px;
    background: var(--panel-white);
  }
  .name {
    position: absolute;
    left: 0;
    width: 712px;
    top: 245px;
    margin: 0;
    text-align: center;
    font-weight: 700;
    font-size: 76px;
    line-height: 1;
    color: var(--card-blue);
  }
  .role {
    position: absolute;
    left: 246px;
    top: 336px;
    margin: 0;
    font-style: italic;
    font-weight: 400;
    font-size: 44px;
    line-height: 1;
    color: var(--card-blue);
  }
  .contact {
    position: absolute;
    left: 262px;
    width: 800px;
    top: 492px;
    margin: 0;
    text-align: center;
    font-weight: 700;
    font-size: 41px;
    line-height: 58px;
    color: var(--ink);
  }
</style>
</head>
<body>
<main class="card">
  <svg class="backdrop" width="1200" height="705" viewBox="0 0 1200 705">
    <defs>
      <linearGradient id="mist-fade" x1="0.75" y1="0" x2="0.1" y2="1">
        <stop offset="0" stop-color="#ffffff"/>
        <stop offset="0.55" stop-color="#f2f7fb"/>
        <stop offset="1" stop-color="var(--mist)"/>
      </linearGradient>
      <linearGradient id="mark-fill" x1="0" y1="0" x2="1" y2="0">
        <stop offset="0" stop-color="var(--teal-light)"/>
        <stop offset="1" stop-color="var(--teal-dark)"/>
      </linearGradient>
    </defs>
    <path class="decor-field" role="img" aria-label="Faint enlarged company mark as background decoration"
          d="M0 392 C150 386 420 392 560 405 C660 420 700 470 700 530 C700 600 690 660 680 705 L0 705 Z"
          fill="url(#mist-fade)"/>
    <circle class="company-mark" role="img" aria-label="Company logo: handset over a striped globe"
            cx="955" cy="270" r="150" fill="url(#mark-fill)"/>
  </svg>

  <div class="name-panel"></div>
  <h1 class="name">Gil Harvey</h1>
  <p class="role">President</p>

  <p class="contact">
    Upland Signal Associates, LLC<br>
    4826-Mercer Drive, Pilot Point<br>
    TX 76490-2817, 972-555-0148
  </p>
</main>
</body>
</html>
```